Professional/modern business card design for construction company

We need a new business card design, double sided keeping it modern, sleek, professional and simple. We are an earthmoving business but do not want any pictures of machinery. I would like one side to have the logo and the other to have all the information, keeping with the colors in our logo. The business card will need to be able to be customised so we can use it for several different managers., we would also like to be able to use the design to apply it to other stationary ie. letterheads, notebooks etc. We do not really have a tag line but we could put on there that we specialise in - Agriculture, Civil Construction and Mining.

Contact Information for Business Card

Brolga Ridge Excavations Pty Ltd
ABN 58 402 937 615
82 Gumleaf Creek Road, Moree NSW 2400

Harold Benton
Managing Director
P 0418 639 204
E haroldbenton@brolgaridgeexc.com.au

Font styles to use
Serif
Sans Serif

Requirements
Nice to have
• I have attached some examples of ideas.
Should not have
• images of machinery

```html
<!DOCTYPE html>
<html lang="en">
<head>
<meta charset="utf-8">
<title>Brolga Ridge Excavations – Business Card</title>
<link rel="stylesheet" href="https://fonts.googleapis.com/css2?family=Montserrat:wght@600;700&family=Lato:wght@300;400&display=swap">
<style>
  :root {
    --backdrop: #262627;
    --card: #49494a;
    --orange: #f7931e;
    --white: #ffffff;
    --soft-white: #e6e6e6;
  }
  * { margin: 0; padding: 0; box-sizing: border-box; }
  html, body { width: 1200px; height: 900px; overflow: hidden; }
  body {
    background: var(--backdrop);
    font-family: "Lato", Arial, sans-serif;
    color: var(--white);
    position: relative;
  }
  .card {
    position: absolute;
    left: 250px;
    width: 700px;
    height: 400px;
    background: var(--card);
    box-shadow: 0 14px 30px rgba(0,0,0,.45);
  }
  .card--front { top: 35px; border-bottom: 6px solid var(--orange); }
  .card--back { top: 465px; }

  /* Front */
  .front-brand {
    position: absolute;
    top: 105px; left: 0; right: 0;
    text-align: center;
  }
  .brand-name {
    font-family: "Montserrat", Arial, sans-serif;
    font-weight: 700;
    color: var(--orange);
    text-transform: uppercase;
    letter-spacing: .5px;
  }
  .front-brand .brand-name { font-size: 30px; line-height: 1.2; }
  .front-brand .brand-mark {
    display: block; width: 18px; height: 18px;
    background: var(--orange); margin: 0 auto 18px;
  }
  .tagline {
    margin-top: 12px;
    font-weight: 300;
    font-size: 19px;
    color: var(--soft-white);
    letter-spacing: .6px;
  }
  .abn {
    font-family: "Montserrat", Arial, sans-serif;
    font-weight: 600;
    font-size: 20px;
    letter-spacing: .6px;
  }
  .abn__label { color: var(--orange); margin-right: 6px; }
  .front-abn { position: absolute; bottom: 45px; left: 0; right: 0; text-align: center; }

  /* Back */
  .back-brand {
    position: absolute;
    top: 40px; right: 40px;
    width: 300px;
    text-align: right;
  }
  .back-brand .brand-name { font-size: 19px; line-height: 1.25; }
  .edge-tab {
    position: absolute; left: 0; top: 150px;
    width: 14px; height: 20px; background: var(--white);
  }
  .person { position: absolute; left: 60px; top: 150px; }
  .person__name {
    font-family: "Montserrat", Arial, sans-serif;
    font-weight: 700;
    font-size: 32px;
    color: var(--orange);
    text-transform: uppercase;
    letter-spacing: .5px;
  }
  .person__title { font-size: 20px; letter-spacing: .8px; margin-top: 2px; }
  .divider {
    position: absolute; left: 240px; right: 45px; top: 228px;
    height: 2px; background: var(--white);
  }
  .contact-list {
    position: absolute; left: 60px; top: 248px;
    list-style: none;
    font-size: 19px; letter-spacing: .7px;
  }
  .contact-list li { display: flex; align-items: center; gap: 14px; height: 34px; }
  .contact-list svg { width: 18px; height: 18px; flex: none; }
  .company-details {
    position: absolute; right: 45px; top: 250px;
    text-align: right; font-size: 20px; line-height: 1.55; letter-spacing: .6px;
  }
  .company-details .abn { font-size: 20px; }
</style>
</head>
<body>

<section class="card card--front">
  <div class="front-brand">
    <span class="brand-mark"></span>
    <p class="brand-name">Brolga Ridge Excavations<br>Pty Ltd</p>
    <p class="tagline">Agriculture, Civil Construction and Mining</p>
  </div>
  <p class="abn front-abn"><span class="abn__label">ABN</span>58 402 937 615</p>
</section>

<section class="card card--back">
  <div class="back-brand">
    <p class="brand-name">Brolga Ridge Excavations Pty Ltd</p>
  </div>
  <span class="edge-tab"></span>
  <div class="person">
    <h1 class="person__name">Harold Benton</h1>
    <p class="person__title">Managing Director</p>
  </div>
  <span class="divider"></span>
  <ul class="contact-list">
    <li>
      <svg viewBox="0 0 18 18" aria-hidden="true"><rect x="4.5" y="1" width="9" height="16" rx="1.5" fill="none" stroke="#f7931e" stroke-width="1.6"/><circle cx="9" cy="14" r="1" fill="#f7931e"/></svg>
      0418 639 204
    </li>
    <li>
      <svg viewBox="0 0 18 18" aria-hidden="true"><rect x="1" y="4" width="16" height="11" fill="#f7931e"/><path d="M1 4 L9 10 L17 4" fill="none" stroke="#49494a" stroke-width="1.4"/></svg>
      haroldbenton@brolgaridgeexc.com.au
    </li>
    <li>
      <svg viewBox="0 0 18 18" aria-hidden="true"><g fill="none" stroke="#f7931e" stroke-width="1.4"><circle cx="9" cy="9" r="7.5"/><ellipse cx="9" cy="9" rx="3.3" ry="7.5"/><path d="M1.5 9h15M3 5h12M3 13h12"/></g></svg>
      www.brolgaridgeexc.com.au
    </li>
  </ul>
  <div class="company-details">
    <p class="abn"><span class="abn__label">ABN</span>58 402 937 615</p>
    <p>82 Gumleaf Creek Road</p>
    <p>Moree NSW 2400</p>
  </div>
</section>

</body>
</html>
```